Environmental "Pledge" Website

We are creating a template for a pledge campaign. Local residents visit a website and fill out a form. If they fill out the form and promise to do something good for the environment, they might win a prize.

They can watch a YouTube video that explains the contest. They can see a Google Map of everybody that has signed the pledge.

There is a blog on the homepage so the can see how the contest is going.

Campaign

```html
<!DOCTYPE html>
<html lang="en">
<head>
<meta charset="UTF-8">
<title>Clear Current – Pledge Campaign</title>
<link href="https://fonts.googleapis.com/css2?family=Didact+Gothic&family=Lato:wght@400;700&display=swap" rel="stylesheet">
<style>
:root{
  --green:#1e7d3e;
  --text:#3a3a3a;
  --nav-text:#6b6b6b;
  --accent:#e8502a;
  --btn:#6d6d6d;
  --rule:#d4d4d4;
  --footer:#3b3b3b;
  --load:#cfcfcf;
}
*{margin:0;padding:0;box-sizing:border-box}
html,body{width:866px;height:1200px;overflow:hidden;background:#fff}
body{position:relative;font-family:'Lato',sans-serif;color:var(--text)}
.hero{position:absolute;left:0;top:0;width:866px;height:419px;
  background:linear-gradient(180deg,#7fb2d9 0%,#a9cbe4 38%,#c9d6de 52%,#9db4c8 70%,#6f87a6 100%)}
.hero::before{content:"";position:absolute;left:0;top:0;width:866px;height:2px;background:var(--accent)}
.nav{position:absolute;left:0;top:2px;width:866px;height:43px;background:rgba(255,255,255,.45);
  display:flex;justify-content:center;gap:23px;font-family:'Didact Gothic',sans-serif;font-size:14px;color:var(--nav-text)}
.nav a{color:inherit;text-decoration:none;line-height:42px;position:relative}
.nav a.active{color:var(--green)}
.nav a.active::after{content:"";position:absolute;left:0;right:0;bottom:0;height:2px;background:var(--green)}
.hero-photo{position:absolute;inset:45px 0 0 0}
.arrow{position:absolute;top:194px;width:31px;height:31px}
.arrow.prev{left:48px}.arrow.next{left:785px}
.promo{position:absolute;left:343px;top:91px;width:179px;height:257px;background:rgba(130,130,130,.72);text-align:center;color:#fff}
.promo .brand{display:flex;align-items:center;justify-content:center;gap:6px;margin-top:72px;font-family:'Didact Gothic',sans-serif;font-size:22px}
.promo .brand i{width:10px;height:10px;border-radius:50%;background:#fff}
.promo p{font-size:10px;font-weight:700;line-height:15px;margin:25px 10px 0}
.promo .cta{display:inline-block;margin-top:20px;width:127px;height:25px;line-height:23px;border:1px solid #eee;background:#3c3c3c;font-size:11.5px;font-weight:700;letter-spacing:.3px}
.band{position:absolute;left:0;top:419px;width:866px;height:280px;background:linear-gradient(#f2f2f2,#fff)}
.section-title{position:absolute;font-family:'Didact Gothic',sans-serif;font-size:21px;color:var(--green);font-weight:400}
.rule{position:absolute;height:1px;background:var(--rule)}
.media{position:absolute;top:489px;width:309px;height:196px}
.video{left:115px;background:linear-gradient(135deg,#f4f1b9 0%,#e8d9a1 35%,#c98a66 65%,#7b3b2a 100%)}
.controls{position:absolute;left:0;bottom:0;width:309px;height:27px;background:#1d1d1d;color:#fff;font-size:11px;font-weight:700}
.controls span{position:absolute;top:8px}
.track{position:absolute;left:67px;top:10px;width:154px;height:7px;border-radius:4px;background:#3b3b3b}
.map{left:441px;background:linear-gradient(90deg,#e8e3d5 0%,#a9c4e0 20%,#a9c4e0 30%,#f0ead2 34%,#f3efe0 100%)}
.blog-title{left:0;width:866px;text-align:center;top:713px}
.post{position:absolute;width:309px;height:115px}
.thumb{position:absolute;left:0;top:0;width:131px;height:115px;border:1px solid #ddd;padding:4px;background:#fff}
.thumb div{width:100%;height:100%}
.post h3{position:absolute;left:143px;top:3px;font-family:'Didact Gothic',sans-serif;font-weight:400;font-size:15px;color:var(--green)}
.post time{position:absolute;left:143px;top:28px;font-size:10.5px}
.post p{position:absolute;left:143px;top:45px;width:170px;font-size:10px;line-height:15.3px}
.post .more{position:absolute;left:143px;top:96px;width:61px;height:19px;line-height:19px;text-align:center;background:var(--btn);color:#fff;font-size:10.5px}
.post::after{content:"";position:absolute;left:0;right:0;bottom:-20px;height:2px;background:linear-gradient(90deg,transparent,#eee,transparent)}
.load{position:absolute;left:115px;top:1109px;width:636px;height:30px;background:var(--load);display:flex;align-items:center;justify-content:center;gap:7px;font-size:10.5px}
.footer{position:absolute;left:0;top:1160px;width:866px;height:40px;background:var(--footer);border-top:2px solid var(--accent);color:#eee;font-size:10.5px;text-align:center;line-height:38px}
</style>
</head>
<body>
<header class="hero">
  <nav class="nav">
    <a class="active" href="#">Home</a><a href="#">About Us</a><a href="#">Fine Print</a><a href="#">Way Pledge</a><a href="#">Pledge Map</a><a href="#">Updates</a>
  </nav>
  <div class="hero-photo" role="img" aria-label="Family running along a sunny beach at the water's edge"></div>
  <svg class="arrow prev" viewBox="0 0 31 31"><circle cx="15.5" cy="15.5" r="15" fill="#555" opacity=".55"/><circle cx="15.5" cy="15.5" r="12" fill="#1c1c1c"/><path d="M17.5 10l-5 5.5 5 5.5" stroke="#fff" stroke-width="1.4" fill="none"/></svg>
  <svg class="arrow next" viewBox="0 0 31 31"><circle cx="15.5" cy="15.5" r="15" fill="#555" opacity=".55"/><circle cx="15.5" cy="15.5" r="12" fill="#1c1c1c"/><path d="M13.5 10l5 5.5-5 5.5" stroke="#fff" stroke-width="1.4" fill="none"/></svg>
  <div class="promo">
    <div class="brand"><i></i>Clear Current</div>
    <p>Lorem ipsum dolor sit amet, ectetuer adipiscing elit, sed diam nonummyeh euismod</p>
    <span class="cta">PLEDGE NOW</span>
  </div>
</header>

<div class="band"></div>
<h2 class="section-title" style="left:115px;top:434px">What's This About</h2>
<div class="rule" style="left:115px;top:473px;width:309px"></div>
<h2 class="section-title" style="left:441px;top:434px">Who's Pledging</h2>
<div class="rule" style="left:441px;top:473px;width:309px"></div>

<div class="media video" role="img" aria-label="Video still of a woman drinking a glass of water">
  <svg style="position:absolute;left:141px;top:80px" width="28" height="28" viewBox="0 0 28 28"><circle cx="14" cy="14" r="13" fill="#555" opacity=".5"/><path d="M11 8l9 6-9 6z" fill="#ddd"/></svg>
  <div class="controls">
    <svg style="position:absolute;left:10px;top:7px" width="12" height="13"><path d="M1 0l11 6.5L1 13z" fill="#fff"/></svg>
    <span style="left:32px">04:59</span>
    <div class="track"><svg style="position:absolute;left:27px;top:-2px" width="11" height="11"><circle cx="5.5" cy="5.5" r="5" fill="#777"/></svg></div>
    <span style="left:224px">10:35</span>
    <svg style="position:absolute;left:256px;top:7px" width="14" height="13"><path d="M1 4h3l4-3v11L4 9H1z" fill="#fff"/><path d="M10 3q3 3.5 0 7" stroke="#fff" fill="none"/></svg>
    <svg style="position:absolute;left:278px;top:7px" width="14" height="14"><path d="M1 1l12 12M1 1h4M1 1v4M13 13h-4M13 13v-4" stroke="#fff" stroke-width="1.5" fill="none"/></svg>
  </div>
</div>
<div class="media map" role="img" aria-label="Street map with a pin marking pledge locations"></div>

<h2 class="section-title blog-title">Latest Blog Posts</h2>
<div class="rule" style="left:278px;top:752px;width:310px"></div>

<article class="post" style="left:115px;top:776px">
  <div class="thumb"><div role="img" aria-label="Child drinking from a water fountain" style="background:linear-gradient(135deg,#5a3a2a,#c23a30 60%,#9aa0a6)"></div></div>
  <h3>Lorem Ipsum Dolor</h3><time>10 Dec 2015</time>
  <p>Lorem ipsum dolor sit amet, ectetuer adipiscing elit, sed diam nonummyeh euismod tincidunt ut laoreet</p>
  <span class="more">Read More</span>
</article>
<article class="post" style="left:441px;top:776px">
  <div class="thumb"><div role="img" aria-label="City skyline at dusk over a marina" style="background:linear-gradient(180deg,#8d8fb8,#c7a3b0 45%,#2c3a2a 70%,#243040)"></div></div>
  <h3>Lorem Ipsum Dolor</h3><time>10 Dec 2015</time>
  <p>Lorem ipsum dolor sit amet, ectetuer adipiscing elit, sed diam nonummyeh euismod tincidunt ut laoreet</p>
  <span class="more">Read More</span>
</article>
<article class="post" style="left:115px;top:948px">
  <div class="thumb"><div role="img" aria-label="Church spire beside a river with a long bridge" style="background:linear-gradient(180deg,#b8c2c8,#9aa6a8 50%,#8a8a78)"></div></div>
  <h3>Lorem Ipsum Dolor</h3><time>10 Dec 2015</time>
  <p>Lorem ipsum dolor sit amet, ectetuer adipiscing elit, sed diam nonummyeh euismod tincidunt ut laoreet</p>
  <span class="more">Read More</span>
</article>
<article class="post" style="left:441px;top:948px">
  <div class="thumb"><div role="img" aria-label="Three generations of a family holding a fish they caught" style="background:linear-gradient(135deg,#6f8a4a,#4a3a2e 50%,#7a8a5a)"></div></div>
  <h3>Lorem Ipsum Dolor</h3><time>10 Dec 2015</time>
  <p>Lorem ipsum dolor sit amet, ectetuer adipiscing elit, sed diam nonummyeh euismod tincidunt ut laoreet</p>
  <span class="more">Read More</span>
</article>

<div class="load">
  <svg width="14" height="14" viewBox="0 0 14 14"><g stroke="#888" stroke-width="1.4" stroke-linecap="round"><path d="M7 1v3M7 10v3M1 7h3M10 7h3M2.8 2.8l2 2M9.2 9.2l2 2M2.8 11.2l2-2M9.2 4.8l2-2"/></g></svg>
  Load More Blog
</div>

<footer class="footer">Copyright © 2015 Clear Current. All Right Reserved.</footer>
</body>
</html>
```